Bluecrest Wellness Group Website

Need a informative, detailed and functional website for a medical cannabis clinic website

check out www.dumelvaclinic.com as competition - want better site than they have

Target Market(s)

Patients

Industry/Entity Type

Health Care

Number of Pages Required

1 page

Font styles to use
Sans Serif

Colors
cadf82
abd036
9bcb3b
3276b5
33a6d7
0392cd
f68d4e

Requirements
Must have
• Clean / Informative
• Will add additional educational content on opioid reduction
Nice to have
• like the white contrast with black/slate dividers. Green logo looks good on slate
• Check documents for ppt regarding website ideas
Should not have
• too many words

```html
<!DOCTYPE html>
<html lang="en">
<head>
<meta charset="utf-8">
<title>Arkansas Bluecrest Wellness Group</title>
<link href="https://fonts.googleapis.com/css2?family=Lato:wght@400;700;900&family=Montserrat:wght@500;600;700&display=swap" rel="stylesheet">
<style>
:root{
  --green:#8cc63f;
  --green-mid:#6fb43a;
  --green-deep:#3d8b3d;
  --title-green:#2f7d3a;
  --lime:#abd036;
  --pale:#cadf82;
  --slate:#3a3a3a;
  --slate-dark:#2b2b2b;
  --ink:#333;
  --muted:#666;
  --red:#e02020;
  --card:#f4f4f4;
}
*{margin:0;padding:0;box-sizing:border-box}
html,body{width:1200px;height:3974px;overflow:hidden}
body{font-family:"Lato",Arial,sans-serif;color:var(--ink);background:#fff;position:relative}
.abs{position:absolute}
.btn{display:inline-block;background:var(--green-mid);color:#fff;border-radius:20px;font-size:15px;font-weight:700;text-align:center;padding:10px 0}
/* top bar */
.topbar{top:0;left:0;width:1200px;height:32px;background:var(--green);color:#fff;font-size:13px}
.topbar .mail{left:100px;top:8px}
.topbar .phone{left:540px;top:8px}
.social{display:flex;gap:8px}
.topbar .social{right:100px;top:0;gap:0}
.topbar .social span{width:36px;height:32px;border-left:1px solid rgba(255,255,255,.4);display:flex;align-items:center;justify-content:center}
.topbar .social i{width:12px;height:12px;border-radius:50%;background:#fff;display:block}
/* header */
.header{top:32px;left:0;width:1200px;height:112px;background:#fff}
.brand{display:flex;align-items:center;gap:12px}
.header .brand{left:85px;top:22px}
.brand .mark{width:52px;height:52px;border-radius:50%;background:var(--green-deep)}
.brand .name{font-family:"Montserrat",sans-serif;font-weight:700;color:var(--green-deep);font-size:15px;line-height:17px;letter-spacing:1px}
.nav{right:100px;top:48px;display:flex;gap:30px;font-size:14px;font-weight:700;font-family:"Montserrat",sans-serif}
.nav a{color:var(--ink);text-decoration:none}
.nav a.active{color:var(--green-mid)}
/* hero */
.hero{top:144px;left:0;width:1200px;height:590px;background:linear-gradient(100deg,#6a6a2e 0%,#b8862c 35%,#f0a93a 55%,#c48a3f 75%,#6d7a3a 100%)}
.hero-title{left:0;width:100%;top:170px;padding-left:0;text-align:left}
.hero-title h1{position:absolute;left:222px;top:0;color:#fff;font-family:"Montserrat",sans-serif;font-weight:700;font-size:32px;white-space:nowrap}
.hero .book{left:222px;top:228px;width:220px}
.hero-card{top:366px;width:244px;height:195px;border-radius:8px;background:rgba(118,190,64,.92);color:#fff;text-align:center;padding:40px 22px 0}
.hero-card .ico{position:absolute;left:98px;top:-24px;width:48px;height:48px;border-radius:50%;background:var(--green-mid);border:3px solid #fff}
.hero-card h3{font-family:"Montserrat",sans-serif;font-size:16px;margin-bottom:8px}
.hero-card p{font-size:12.5px;line-height:16px}
.hero-card .btn{position:absolute;left:38px;bottom:22px;width:168px;border-radius:2px;background:#5a9b2c;font-size:13px;padding:9px 0}
/* welcome intro */
.intro{top:790px;left:85px;width:410px;text-align:center}
.intro .small{font-size:14px;font-weight:700;font-family:"Montserrat",sans-serif}
.intro h2{font-family:"Montserrat",sans-serif;color:var(--title-green);letter-spacing:5px;font-size:26px;margin-top:14px}
.intro h3{font-family:"Montserrat",sans-serif;color:var(--green-mid);letter-spacing:3px;font-size:16px;margin-top:6px}
.intro p{font-size:14px;line-height:21px;text-align:left;margin-top:22px;padding:0 20px}
.perks{top:1005px;left:85px;width:410px;display:flex;justify-content:space-around}
.perk{text-align:center;font-size:13px}
.perk svg{display:block;margin:0 auto 8px}
.map{left:560px;top:760px;width:580px;height:290px;background:linear-gradient(135deg,#9ccd3c,#d7d7d7 50%,#7cb83a);border-radius:4px}
.legend{left:820px;top:1055px;font-size:11px;line-height:20px}
.legend i{display:inline-block;width:14px;height:10px;margin-right:6px;vertical-align:middle}
/* features */
.feature{top:1227px;width:318px;height:403px;background:var(--card);text-align:center}
.feature .photo{height:195px}
.feature h3{font-family:"Montserrat",sans-serif;font-weight:600;font-size:19px;margin:20px 0 16px}
.feature p{font-size:14px;line-height:19px;padding:0 32px;text-align:left}
.feature .btn{position:absolute;left:79px;bottom:22px;width:160px;font-size:14px;padding:8px 0}
/* qualify */
.qualify{top:1700px;left:0;width:1200px;height:560px;background:radial-gradient(ellipse at 50% 40%,#2f4a1e 0%,#16210e 60%,#0c120a 100%)}
.qualify h2{position:absolute;top:36px;width:100%;text-align:center;color:#fff;font-family:"Montserrat",sans-serif;font-size:32px;font-weight:600}
.loc{top:110px;width:312px;height:366px;background:#fff;border:6px solid #fff;text-align:center;font-size:15px}
.loc.featured{border-color:var(--green-deep);background:#eef4e8}
.loc h3{background:var(--green-mid);color:#fff;font-family:"Montserrat",sans-serif;font-size:26px;font-weight:700;height:68px;line-height:68px}
.loc .from{margin-top:16px}
.loc .price{color:var(--red);font-size:28px;font-weight:900;margin:2px 0 10px}
.loc .rule{width:210px;height:1px;background:var(--green-mid);margin:0 auto 14px}
.loc .addr{color:var(--green-deep);line-height:20px;margin-bottom:12px}
.loc .note{line-height:20px}
.loc .btn{position:absolute;left:72px;bottom:22px;width:156px;font-size:14px;padding:8px 0}
.dots{top:528px;left:574px;display:flex;gap:6px}
.dots i{width:8px;height:3px;background:#777;display:block}
/* steps */
.steps-title{top:2308px;width:1200px;text-align:center;font-family:"Montserrat",sans-serif;font-weight:500;font-size:32px;line-height:42px}
.step{top:2420px;width:220px;text-align:center;font-size:20px;line-height:24px}
.step .circle{width:104px;height:104px;border-radius:50%;background:var(--green-mid);margin:0 auto 16px;display:flex;align-items:center;justify-content:center}
.arrow{top:2450px}
/* about */
.about{top:2670px;left:0;width:1200px;text-align:center}
.about .small{font-family:"Montserrat",sans-serif;font-weight:700;font-size:22px}
.about h2{font-family:"Montserrat",sans-serif;color:var(--title-green);font-size:44px;letter-spacing:8px;margin-top:16px}
.about h3{font-family:"Montserrat",sans-serif;color:var(--green-mid);font-size:30px;letter-spacing:6px;margin-top:2px}
.divider{display:flex;align-items:center;justify-content:center;gap:14px;margin-top:14px}
.divider i{width:120px;height:3px;background:var(--green-deep);display:block}
.divider b{width:56px;height:56px;border-radius:50%;background:var(--green-deep);display:block}
.about p{width:1030px;margin:30px auto 0;font-size:15px;line-height:24px}
.about p+p{margin-top:22px}
.about .btn{width:196px;margin-top:34px;font-size:15px}
/* help & newsletter */
.help{top:3305px;left:0;width:600px;height:305px;background:var(--green-mid);color:#fff;padding:50px 0 0 78px}
.help h2,.news h2{font-family:"Montserrat",sans-serif;font-size:30px;font-weight:600}
.help .line{width:460px;height:1px;background:rgba(255,255,255,.6);margin:14px 0 18px}
.help .row{font-size:15px;display:flex;align-items:center;gap:14px;margin:12px 0 0}
.news{top:3305px;left:600px;width:600px;height:305px;background:var(--lime);color:#fff;padding:50px 0 0 66px}
.news p{font-size:15px;line-height:22px;margin-top:14px;width:470px}
.news .field{margin-top:26px;width:458px;height:54px;background:#fff;border-radius:27px;color:#555;font-size:14px;display:flex;align-items:center;justify-content:space-between;padding:0 10px 0 26px}
.news .field b{width:38px;height:38px;border-radius:50%;background:var(--green-mid);display:flex;align-items:center;justify-content:center}
/* footer */
.footer{top:3610px;left:0;width:1200px;height:272px;background:var(--slate);color:#fff;font-size:13px}
.footer .fbrand{left:80px;top:52px;background:#fff;width:222px;height:90px;padding:0 14px;display:flex;align-items:center}
.footer .fbrand .name{font-size:13px;line-height:15px}
.footer .fbrand .mark{width:44px;height:44px}
.footer .about-txt{left:80px;top:155px;width:230px;line-height:18px}
.footer .more{left:80px;top:222px}
.footer h4{font-family:"Montserrat",sans-serif;font-size:18px;font-weight:600;margin-bottom:14px}
.footer ul{list-style:none;line-height:19px}
.footer ul li::before{content:"•";margin-right:8px;color:var(--green)}
.quick{left:370px;top:60px}
.company{left:575px;top:60px;line-height:20px}
.contact{left:830px;top:60px}
.contact .inputs{display:flex;gap:8px}
.contact .inputs span,.contact .msg{background:#555;border:1px solid #777;color:#ddd;font-size:12px;padding:5px 8px}
.contact .inputs span{width:92px}
.contact .msg{width:292px;height:66px;margin-top:10px}
.contact .btn{margin-top:12px;width:140px;font-size:13px;padding:7px 0}
.bottombar{top:3882px;left:0;width:1200px;height:92px;background:#fff;font-size:13px}
.bottombar .copy{left:80px;top:38px}
.bottombar .social{right:100px;top:30px}
.bottombar .social i{width:28px;height:28px;border-radius:50%;background:var(--green-deep);display:block}
</style>
</head>
<body>

<div class="abs topbar">
  <div class="abs mail">✉&nbsp; info@bluecrestwellness.com</div>
  <div class="abs phone">☏&nbsp; +123 456 7890</div>
  <div class="abs social"><span><i></i></span><span><i></i></span><span><i></i></span><span><i></i></span><span><i></i></span></div>
</div>

<header class="abs header">
  <div class="abs brand"><span class="mark"></span><span class="name">ARKANSAS<br>BLUECREST<br>WELLNESS GROUP</span></div>
  <nav class="abs nav"><a class="active">HOME</a><a>ABOUT</a><a>QUALIFY</a><a>APPOINTMENTS</a><a>FAQ</a><a>CONTACT</a><a>NEWS</a></nav>
</header>

<section class="abs hero" role="img" aria-label="Woman with outstretched arms in warm sunset light over green hills">
  <div class="abs hero-title"><h1>NOW TAKING APPOINTMENTS</h1></div>
  <span class="abs btn book">BOOK APPOINTMENTS</span>
  <div class="abs hero-card" style="left:218px"><span class="ico"></span><h3>100% RISK FREE</h3><p>Lorem Ipsum is simply dummy text of the printing and typesetting a ever since the 1500s</p><span class="btn">Book Online</span></div>
  <div class="abs hero-card" style="left:478px;background:rgba(80,180,90,.92)"><span class="ico"></span><h3>FAQ</h3><p>Lorem Ipsum is simply dummy text of the printing and typesetting a ever since the 1500s</p><span class="btn">Read More</span></div>
  <div class="abs hero-card" style="left:738px"><span class="ico"></span><h3>OPIOID REDUCTION</h3><p>Lorem Ipsum is simply dummy text of the printing and typesetting a ever since the 1500s</p><span class="btn">Read More</span></div>
</section>

<section class="abs intro">
  <div class="small">WELCOME TO</div>
  <h2>ARKANSAS</h2>
  <h3>BLUECREST WELLNESS GROUP</h3>
  <p>Lorem Ipsum is simply dummy ever text the printing and typesetting a ever since the 1500s</p>
</section>
<div class="abs perks">
  <div class="perk"><svg width="34" height="34" viewBox="0 0 34 34"><circle cx="17" cy="17" r="13" fill="none" stroke="#333" stroke-width="3"/><path d="M17 9v9l6 4" stroke="#333" stroke-width="3" fill="none"/></svg>Fast &amp; Easy</div>
  <div class="perk"><svg width="34" height="34" viewBox="0 0 34 34"><circle cx="17" cy="17" r="14" fill="#333"/><path d="M10 17l5 5 9-10" stroke="#fff" stroke-width="3" fill="none"/></svg>Quality</div>
  <div class="perk"><svg width="34" height="34" viewBox="0 0 34 34"><rect x="5" y="8" width="24" height="18" rx="3" fill="#333"/><circle cx="17" cy="17" r="4" fill="#fff"/></svg>Inexpensive</div>
  <div class="perk"><svg width="34" height="34" viewBox="0 0 34 34"><path d="M11 15v-4a6 6 0 0112 0v4" stroke="#333" stroke-width="3" fill="none"/><rect x="7" y="15" width="20" height="15" rx="2" fill="#333"/></svg>Assurance</div>
</div>
<div class="abs map" role="img" aria-label="Map of the United States showing states with legal medical and recreational marijuana"></div>
<div class="abs legend"><div><i style="background:#9ccd3c"></i>States with Legal Medical Marijuana</div><div><i style="background:#3d8b3d"></i>States with Legal Medical Marijuana and Recreational Marijuana</div></div>

<article class="abs feature" style="left:85px"><div class="photo" role="img" aria-label="Hands writing on paper beside a laptop" style="background:linear-gradient(135deg,#cfd8e0,#8da2b4)"></div><h3>No Qualification? No Fee</h3><p>Lorem Ipsum is simply dummy text of the printing and typesetting. Lorem Ipsum has been the industry's standard dummy text ever since the 1500s</p><span class="btn">Read More</span></article>
<article class="abs feature" style="left:441px"><div class="photo" role="img" aria-label="Physician in a white coat in a clinic" style="background:linear-gradient(135deg,#e6ecef,#a9b9c2)"></div><h3>Qualified Physicians</h3><p>Lorem Ipsum is simply dummy text of the printing and typesetting. Lorem Ipsum has been the industry's standard dummy text ever since the 1500s</p><span class="btn">Read More</span></article>
<article class="abs feature" style="left:797px"><div class="photo" role="img" aria-label="Doctor consulting a patient" style="background:linear-gradient(135deg,#d9cfc4,#8fa5b5)"></div><h3>Convenience</h3><p>Lorem Ipsum is simply dummy text of the printing and typesetting. Lorem Ipsum has been the industry's standard dummy text ever since the 1500s</p><span class="btn">Read More</span></article>

<section class="abs qualify" role="img" aria-label="Dark background of green cannabis plants">
  <h2>Do I Qualify?</h2>
  <div class="abs loc" style="left:85px"><h3>Little Rock</h3><div class="from">Certification as low as</div><div class="price">$20/mo*</div><div class="rule"></div><div class="addr">2480 Harlow Avenue<br>Suite B-2, Little Rock, AR 72205</div><div class="rule"></div><div class="note">We are now accepting<br>appointments at our Little<br>Rock location.</div><span class="btn">Appointments</span></div>
  <div class="abs loc featured" style="left:444px"><h3>N. Little Rock</h3><div class="from">Certification as low as</div><div class="price">$20/mo*</div><div class="rule"></div><div class="addr">Estimated Launch<br>In May</div><div class="rule"></div><div class="note">Please stay tuned for<br>updates</div><span class="btn">Appointments</span></div>
  <div class="abs loc" style="left:803px"><h3>Hot Springs</h3><div class="from">Certification as low as</div><div class="price">$20/mo*</div><div class="rule"></div><div class="addr">Estimated Launch<br>In May</div><div class="rule"></div><div class="note">Please stay tuned for<br>updates</div><span class="btn">Appointments</span></div>
  <div class="abs dots"><i></i><i></i><i></i></div>
</section>

<h2 class="abs steps-title">3 Steps to Get Your Arkansas<br>Marijuana Card</h2>
<div class="abs step" style="left:248px"><div class="circle"><svg width="54" height="54" viewBox="0 0 54 54" fill="none" stroke="#fff" stroke-width="3"><circle cx="27" cy="18" r="9"/><path d="M10 48c0-10 8-16 17-16s17 6 17 16z"/></svg></div>Meet a Marijuana<br>Doctor</div>
<svg class="abs arrow" style="left:442px" width="80" height="40" viewBox="0 0 80 40"><path d="M4 30 Q40 4 66 18" stroke="#6fb43a" stroke-width="6" fill="none"/><path d="M58 6l18 14-22 6z" fill="#6fb43a"/></svg>
<div class="abs step" style="left:500px"><div class="circle"><svg width="58" height="50" viewBox="0 0 58 50" fill="none" stroke="#fff" stroke-width="3"><rect x="4" y="6" width="50" height="38" rx="4"/><path d="M14 36h30M20 16h18v12H20z"/></svg></div>Apply for Marijuana<br>Card</div>
<svg class="abs arrow" style="left:700px" width="80" height="40" viewBox="0 0 80 40"><path d="M4 30 Q40 4 66 18" stroke="#6fb43a" stroke-width="6" fill="none"/><path d="M58 6l18 14-22 6z" fill="#6fb43a"/></svg>
<div class="abs step" style="left:770px"><div class="circle"><svg width="54" height="54" viewBox="0 0 54 54" fill="none" stroke="#fff" stroke-width="3"><rect x="6" y="10" width="40" height="36" rx="3"/><path d="M6 20h40M16 5v10M36 5v10"/><circle cx="38" cy="38" r="9" fill="#6fb43a"/><path d="M38 33v6l4 2"/></svg></div>Follow-up<br>Appointment</div>

<section class="abs about">
  <div class="small">WELCOME TO</div>
  <h2>ARKANSAS BLUECREST</h2>
  <h3>WELLNESS GROUP</h3>
  <div class="divider"><i></i><b></b><i></i></div>
  <p>Bluecrest Clinic came into existence in 2018 following the legalization of medical marijuana for qualifying conditions in Arkansas. Our marijuana doctors have years of experience treating chronically ill patients in a variety of practice settings. Currently, most patients suffering from painful and debilitating conditions are treated with addictive or ineffective medicines such as narcotics without first being given the option to try a natural solution such as medical cannabis. Our marijuana doctors understand your challenges and will help you navigate your options with medical cannabis.</p>
  <p>Our marijuana doctors ( Cannabis doctor ) and staff are here to provide you with the best medical care for anyone who is seeking a healthier alternative to addictive, harmful pain medicines used today. Our job is to educate and help you understand the process in which to obtain your Arkansas marijuana card ( cannabis card ) so that you may finally have all options to better take control of your health.</p>
  <span class="btn">Read More</span>
</section>

<section class="abs help">
  <h2>Need Help?</h2>
  <div class="line"></div>
  <div class="row">✉&nbsp; | &nbsp;contact@bluecrestwellness.com</div>
  <div class="row">☏&nbsp; | &nbsp;+00 123 456 7890</div>
  <div class="row">◷&nbsp; | &nbsp;Monday - Saturday 9:00 -18:00hrs.</div>
</section>
<section class="abs news">
  <h2>Newsletter Signup</h2>
  <p>Please subscribe and receive our latest news, promotions, events, and clinic updates you can't get anywhere else.</p>
  <div class="field">Enter your email here*<b><svg width="18" height="18" viewBox="0 0 18 18"><path d="M1 8l16-7-6 16-3-6z" fill="#fff"/></svg></b></div>
</section>

<footer class="abs footer">
  <div class="abs fbrand brand"><span class="mark"></span><span class="name">ARKANSAS<br>BLUECREST<br>WELLNESS GROUP</span></div>
  <div class="abs about-txt">Lorem Ipsum is simply dummy text of the printing and typesetting Ads and in the industry</div>
  <div class="abs more">Read More ⊙</div>
  <div class="abs quick"><h4>Quick Link</h4><ul><li>Home</li><li>About us</li><li>Services</li><li>Testimonial</li><li>Blogs</li><li>Contact us</li><li>Privacy/Terms</li></ul></div>
  <div class="abs company"><h4>Company address</h4>⌖ Arkansas Bluecrest Wellness<br>&nbsp;&nbsp;&nbsp;4410 Maple Crest Drive Suite 210<br>&nbsp;&nbsp;&nbsp;Conway, USA<br>☏ 0- (123) 456-7890<br>☏ 0- (123) 456-7890<br>☏ 0- (123) 456-7890<br>✉ info@ domainname.com</div>
  <div class="abs contact"><h4>Contact us</h4><div class="inputs"><span>Name</span><span>Email</span><span>Phone</span></div><div class="msg">Message</div><span class="btn">Subscribe</span></div>
</footer>
<div class="abs bottombar">
  <div class="abs copy">CopyRight © 2019 Arkansas Bluecrest Wellness Group. All Right Reserve</div>
  <div class="abs social"><i></i><i></i><i></i><i></i><i></i></div>
</div>

</body>
</html>
```